Vintage-style label for a tube cake pan

We are looking for designs for a 1950-1960s vintage-style label for a cake pan. I've attached examples from other older cake pans. The last two photos are the image we've identified as the one that best encapsulates our brand and an illustration of the pan.

You can leave a placeholder for the logo, and you can use the words below in your design (feel free to pick and choose):

Product title:
Square Tube Cake Pan
Product subtitle:
for Angel Food Cakes and Mile High Pound Cakes
Product Attributes:
Holds 18 cups of batter for mile high cakes
Even-heating aluminum for the highest rise
Resists rust and abrasions
Family-owned and operated company
Two pieces for easy removal
9 in x 9 in x 4.5 in
For recipes and care instructions SEE REVERSE SIDE

The dimensions for the label are 7.5 in x 7.5 in with a 2.4 in hole in the center
Updates

Designs look the same

Target Market(s)

American grandmas

Requirements
Must have
• Should feel authentically vintage to American ads in the 1950s and 1960s

```html
<!DOCTYPE html>
<html lang="en">
<head>
<meta charset="utf-8">
<title>Hearthwell Square Tube Cake Pan Label</title>
<link rel="stylesheet" href="https://fonts.googleapis.com/css2?family=Chewy&family=Leckerli+One&family=Libre+Baskerville:wght@400;700&family=Oswald:wght@500;600&display=swap">
<style>
  :root {
    --cream: #fdf3dc;
    --butter: #f6c766;
    --tomato: #e0101a;
    --cocoa: #7a3416;
    --rust: #a0401a;
    --ink: #3a2a22;
    --white: #ffffff;
    --wood-dark: #5a3620;
    --wood: #9a6436;
    --wall: #d8c6a6;
    --stove: #3a2c24;
  }
  html, body { margin: 0; padding: 0; width: 1200px; height: 1000px; overflow: hidden; background: var(--white); }
  .label { position: absolute; left: 229px; top: 128px; width: 743px; height: 743px; overflow: hidden; background: var(--cream); }
  .kitchen-scene { position: absolute; left: 0; top: 0; width: 743px; height: 470px;
    background:
      linear-gradient(180deg, rgba(90,54,32,0.85) 0%, rgba(90,54,32,0) 22%),
      radial-gradient(ellipse 260px 180px at 420px 260px, rgba(232,220,198,0.95), rgba(232,220,198,0) 100%),
      linear-gradient(90deg, var(--wood) 0%, #b27a46 22%, var(--wall) 45%, #c9b08a 70%, #6b4a34 100%),
      linear-gradient(180deg, transparent 70%, var(--stove) 100%);
    background-blend-mode: normal; }
  .shapes { position: absolute; left: 0; top: 0; }
  .brand-name { position: absolute; left: 90px; top: 62px; width: 560px; text-align: center; margin: 0;
    font-family: "Leckerli One", "Chewy", cursive; font-weight: 400; font-size: 100px; line-height: 1;
    color: var(--tomato); transform: rotate(8deg); }
  .subtitle { position: absolute; left: 140px; top: 190px; width: 480px; text-align: center; margin: 0;
    font-family: "Chewy", "Leckerli One", cursive; font-size: 30px; line-height: 1.05; color: var(--white);
    letter-spacing: 0.5px; transform: rotate(8deg);
    text-shadow: -2px -2px 0 #111, 2px -2px 0 #111, -2px 2px 0 #111, 2px 2px 0 #111, 0 4px 0 #111; }
  .pan-thumb { position: absolute; left: 14px; top: 237px; width: 90px; height: 56px; border-radius: 6px;
    background: linear-gradient(135deg, #d7dadc, #8d9296); transform: rotate(-8deg); }
  .badge-text { position: absolute; left: 2px; top: 300px; width: 170px; text-align: center; margin: 0;
    font-family: "Libre Baskerville", serif; color: #111; transform: rotate(-22deg); line-height: 1.05; }
  .badge-text .line-small { font-weight: 700; font-size: 14px; display: block; }
  .badge-text .line-big { font-weight: 700; font-size: 19px; display: block; }
  .badge-text .line-size { font-weight: 400; font-size: 12px; display: block; }
  .cake-art { position: absolute; left: 17px; top: 409px; width: 425px; height: 268px; border-radius: 50% 50% 20px 20px / 30% 30% 20px 20px;
    background: linear-gradient(170deg, #fbf6ea 0%, #f3e4c0 30%, #f0d28a 50%, #b07a4a 80%, #7d4f2e 100%); }
  .center-hole { position: absolute; left: 280px; top: 280px; width: 182px; height: 182px; border-radius: 50%;
    background: rgba(255,255,255,0.72); }
  .tagline { position: absolute; left: 440px; top: 474px; width: 280px; margin: 0;
    font-family: "Chewy", "Leckerli One", cursive; font-weight: 400; font-size: 42px; line-height: 0.95;
    color: var(--cocoa); transform: rotate(-3deg); }
  .features { position: absolute; left: 459px; top: 559px; margin: 0; padding: 0; list-style: none;
    font-family: "Oswald", sans-serif; font-weight: 600; font-size: 12px; line-height: 17.5px;
    text-transform: uppercase; color: var(--ink); }
  .reverse-note { position: absolute; left: 459px; top: 655px; margin: 0; font-family: "Oswald", sans-serif; font-weight: 500;
    font-size: 13px; color: var(--rust); white-space: nowrap; }
  .reverse-note .reverse-tag { display: inline-block; margin-left: 6px; padding: 2px 8px; background: var(--cocoa);
    color: var(--white); font-weight: 600; font-size: 11px; transform: rotate(-3deg); }
  .benefits { position: absolute; left: 0; top: 702px; width: 743px; text-align: center; margin: 0;
    font-family: "Chewy", "Leckerli One", cursive; font-size: 20px; letter-spacing: 0.3px; color: var(--cocoa); }
</style>
</head>
<body>
<main class="label">
  <div class="kitchen-scene" role="img" aria-label="Vintage farmhouse kitchen with wooden shelves, hanging pots and an old stove"></div>

  <svg class="shapes" width="743" height="743" viewBox="0 0 743 743" aria-hidden="true">
    <path fill="var(--cream)" d="M-30 470 a44 44 0 0 1 88 0 a44 44 0 0 1 88 0 a44 44 0 0 1 88 0 a44 44 0 0 1 88 0 a44 44 0 0 1 88 0 a44 44 0 0 1 88 0 a44 44 0 0 1 88 0 a44 44 0 0 1 88 0 a44 44 0 0 1 88 0 L800 743 L-30 743 Z"/>
    <path fill="var(--butter)" d="M-20 692 a44 26 0 0 1 88 0 a44 26 0 0 1 88 0 a44 26 0 0 1 88 0 a44 26 0 0 1 88 0 a44 26 0 0 1 88 0 a44 26 0 0 1 88 0 a44 26 0 0 1 88 0 a44 26 0 0 1 88 0 a44 26 0 0 1 88 0 L800 743 L-20 743 Z"/>
    <polygon fill="var(--butter)" points="83,242 95,262 113,248 117,270 138,262 134,284 156,284 145,303 166,310 150,324 168,337 148,347 161,365 139,368 145,390 124,385 121,407 103,396 92,415 80,396 63,410 58,388 38,395 41,373 19,374 29,354 9,345 27,332 11,316 32,308 21,289 43,286 40,264 61,270 64,248"/>
  </svg>

  <div class="pan-thumb" role="img" aria-label="Small illustration of the square aluminum tube pan"></div>
  <p class="badge-text"><span class="line-small">SQUARE TUBE</span><span class="line-big">CAKE PAN</span><span class="line-size">STANDARD SIZE</span></p>

  <h1 class="brand-name">Hearthwell</h1>
  <p class="subtitle">for Angel Food Cakes and<br>Mile High Pound Cakes</p>

  <div class="cake-art" role="img" aria-label="Engraved illustration of a frosted cake with a slice topped with strawberries and chocolate"></div>
  <div class="center-hole" aria-hidden="true"></div>

  <h2 class="tagline">Baking with a<br>Vintage Twist</h2>
  <ul class="features">
    <li>Holds 18 cups of batter for mile high cakes</li>
    <li>Even-heating aluminum for the highest rise</li>
    <li>Resists rust and abrasions</li>
    <li>Family-owned and operated company</li>
    <li>Two pieces for easy removal</li>
  </ul>
  <p class="reverse-note">For recipes and care instructions <span class="reverse-tag">SEE REVERSE SIDE</span></p>

  <p class="benefits">Perfect Even Baking - Effortless Release - Nostalgic Vintage Design</p>
</main>
</body>
</html>
```